Quartz Owl needs Bad-Ass Design!
Professional
Thos. Carl Pemberton
Owner
P.O. Box 27815 Lanai Point, HI. 96218
carlpemberton@k9ventura.us.com
http://www.k9ventura.us.com

```html
<!DOCTYPE html>
<html lang="en">
<head>
<meta charset="utf-8">
<title>Quartz Owl — Business Card</title>
<link rel="stylesheet" href="https://fonts.googleapis.com/css2?family=Source+Sans+3:wght@400;600;700&display=swap">
<style>
  :root {
    --page-bg: #ece7df;
    --card-bg: #ffffff;
    --card-edge: #d9d4cc;
    --brand-navy: #1f3f78;
    --accent-red: #d8262c;
    --text-dark: #333333;
    --text-mid: #4a4a4a;
    --icon-blue: #2a5592;
  }
  * { margin: 0; padding: 0; box-sizing: border-box; }
  html, body {
    width: 1200px;
    height: 965px;
    overflow: hidden;
    background: var(--page-bg);
    font-family: "Source Sans 3", Arial, sans-serif;
  }
  .business-card {
    position: absolute;
    left: 240px;
    top: 230px;
    width: 774px;
    height: 440px;
    background: var(--card-bg);
    border: 1px solid var(--card-edge);
    border-radius: 26px;
    box-shadow: 0 6px 18px rgba(0, 0, 0, 0.12);
  }
  .brand {
    position: absolute;
    left: 40px;
    top: 44px;
  }
  .brand-row {
    display: flex;
    align-items: center;
    gap: 14px;
  }
  .brand-mark {
    width: 30px;
    height: 30px;
    background: var(--brand-navy);
  }
  .brand-name {
    font-size: 52px;
    font-weight: 600;
    line-height: 1;
    color: var(--brand-navy);
    letter-spacing: -0.5px;
  }
  .brand-tagline {
    margin: 2px 0 0 143px;
    font-size: 17px;
    font-weight: 700;
    color: var(--text-dark);
  }
  .person {
    position: absolute;
    left: 40px;
    top: 166px;
  }
  .person-name {
    font-size: 32px;
    font-weight: 700;
    color: var(--brand-navy);
    line-height: 1.1;
  }
  .person-role {
    font-size: 19px;
    font-weight: 700;
    color: var(--accent-red);
    margin-top: 0;
    line-height: 1.2;
  }
  .contact {
    position: absolute;
    left: 40px;
    top: 270px;
    font-size: 21px;
    color: var(--text-mid);
  }
  .contact-address { height: 32px; line-height: 32px; margin-bottom: 2px; }
  .contact-line {
    display: flex;
    align-items: center;
    gap: 10px;
    height: 32px;
  }
  .contact-icon {
    width: 18px;
    height: 18px;
    flex: none;
  }
</style>
</head>
<body>
  <article class="business-card">
    <header class="brand">
      <div class="brand-row">
        <div class="brand-mark"></div>
        <div class="brand-name">K9 Ventura</div>
      </div>
      <div class="brand-tagline">Tech help all day and night</div>
    </header>

    <section class="person">
      <h1 class="person-name">Thos. Carl Pemberton</h1>
      <div class="person-role">Owner</div>
    </section>

    <section class="contact">
      <div class="contact-address">P.O. Box 27815&nbsp; Lanai Point, HI. 96218</div>
      <div class="contact-line">
        <svg class="contact-icon" viewBox="0 0 24 24" aria-hidden="true">
          <path d="M6.6 10.8a15.1 15.1 0 0 0 6.6 6.6l2.2-2.2a1 1 0 0 1 1-.25 11.4 11.4 0 0 0 3.6.57 1 1 0 0 1 1 1V20a1 1 0 0 1-1 1A17 17 0 0 1 3 4a1 1 0 0 1 1-1h3.5a1 1 0 0 1 1 1c0 1.25.2 2.45.57 3.57a1 1 0 0 1-.25 1z" fill="var(--icon-blue)"/>
        </svg>
        <span>(555) 214-0147</span>
      </div>
      <div class="contact-line">
        <svg class="contact-icon" viewBox="0 0 24 24" aria-hidden="true">
          <text x="12" y="19" text-anchor="middle" font-size="22" font-weight="700" fill="var(--icon-blue)" font-family="Arial, sans-serif">@</text>
        </svg>
        <span>carlpemberton@k9ventura.us.com</span>
      </div>
      <div class="contact-line">
        <svg class="contact-icon" viewBox="0 0 24 24" aria-hidden="true">
          <circle cx="12" cy="12" r="10" fill="none" stroke="var(--icon-blue)" stroke-width="2"/>
          <ellipse cx="12" cy="12" rx="4.5" ry="10" fill="none" stroke="var(--icon-blue)" stroke-width="1.6"/>
          <line x1="2" y1="12" x2="22" y2="12" stroke="var(--icon-blue)" stroke-width="1.6"/>
          <line x1="4" y1="7" x2="20" y2="7" stroke="var(--icon-blue)" stroke-width="1.3"/>
          <line x1="4" y1="17" x2="20" y2="17" stroke="var(--icon-blue)" stroke-width="1.3"/>
        </svg>
        <span>www.k9ventura.us.com</span>
      </div>
    </section>
  </article>
</body>
</html>
```